Nobre Lente Lusitana - business card

Create a business card for my eyewear (glasses) store. The concept is based in handcrafted glasses (as well as common frames and 3d printed), clean, and elegant. The business card could be black (white letters and symbols) or white (black letters and symbols) but we are open to new suggestions. It must be sober and elegant.
The name Nobre Lente Lusitana means Royal/Real Portuguese Optical Store.
Our concept should be inspired by the pictures attatched bellow.
I would like it to be classic and elegant as business cards for bankers.
Our first selected logo is also available in attachment files.

Target Market(s)

For business meetings with investors, supliers and fairs

Industry/Entity Type

Eyewear

Contact Information for Business Card

Some random business cards in attachment that we like. Don't be closed to it, we like freedom of think.

Font styles to use
Serif
Sans Serif

Colors
404040
e9e9e9
fbfbfb
000000
85abd3
0255a3
f7fbfd
959595

Requirements
Must have
• Must be elegant, simple.
• Must present our brand new logo (slight variations are welcome, the logo is not closed yet). See our temporary logo in attachment.
• Black (or dark grey), white (or light grey) and a third slight color.
• This third slight color could be dark blue or grayish blue.
• Info:
• Fernando Amaral (name)
• famaral@nobrelentelusitana.example
• +351 936204518
• www.nobrelentelusitana.example
Nice to have
• Black and white or with serious colors such as dark blue or greyish blue.
• Could also have water mark with our logo (big size) in the background (inspired in KVN bank credit card design)
Should not have
• Hysteric colora or shapes

```html
<!DOCTYPE html>
<html lang="pt">
<head>
<meta charset="utf-8">
<title>Nobre Lente Lusitana — Cartão de visita</title>
<link rel="stylesheet" href="https://fonts.googleapis.com/css2?family=Roboto+Slab:wght@500;700&family=Roboto:wght@400&display=swap">
<style>
  :root {
    --ink: #000000;
    --paper: #fbfbfb;
    --text-grey: #404040;
    --stage: #e9e9e9;
    --white: #ffffff;
    --accent-blue: #0255a3;
    --accent-blue-soft: #85abd3;
  }
  * { box-sizing: border-box; margin: 0; padding: 0; }
  html, body { width: 1200px; height: 800px; overflow: hidden; }
  body {
    background: var(--stage);
    display: flex;
    align-items: center;
    justify-content: center;
    gap: 48px;
  }
  .card {
    position: relative;
    width: 520px;
    height: 297px;
    overflow: hidden;
    box-shadow: 0 2px 10px rgba(0,0,0,0.12);
  }
  .card--front { background: var(--paper); color: var(--ink); }
  .card--back {
    background: var(--ink);
    color: var(--white);
    display: flex;
    align-items: center;
    justify-content: center;
  }

  .name-band {
    position: absolute;
    top: 34px;
    right: 0;
    width: 230px;
    height: 40px;
    background: var(--ink);
    clip-path: polygon(14px 0, 100% 0, 100% 100%, 0 100%);
    display: flex;
    align-items: center;
    justify-content: center;
    padding-left: 14px;
    border-bottom: 3px solid var(--accent-blue);
  }
  .name-band__text {
    font-family: "Roboto Slab", serif;
    font-weight: 700;
    font-size: 16px;
    letter-spacing: 0.5px;
    color: var(--white);
    text-transform: uppercase;
    white-space: nowrap;
  }

  .brand-name {
    font-family: "Roboto Slab", serif;
    font-weight: 500;
    text-transform: uppercase;
    line-height: 1.25;
  }
  .card--front .brand-name {
    position: absolute;
    left: 40px;
    top: 118px;
    font-size: 17px;
    letter-spacing: 4px;
  }
  .card--back .brand-name {
    font-size: 26px;
    letter-spacing: 7px;
    text-align: center;
  }

  .contact-list {
    position: absolute;
    left: 40px;
    bottom: 30px;
    list-style: none;
    font-family: "Roboto", sans-serif;
    font-size: 13px;
    color: var(--text-grey);
  }
  .contact-list__item {
    display: flex;
    align-items: center;
    gap: 9px;
    line-height: 20px;
    white-space: nowrap;
  }
  .contact-list__icon { width: 11px; height: 11px; fill: var(--accent-blue); flex: none; }
</style>
</head>
<body>
  <article class="card card--front">
    <div class="name-band"><span class="name-band__text">Fernando Amaral</span></div>

    <p class="brand-name">Nobre<br>Lente<br>Lusitana</p>

    <ul class="contact-list">
      <li class="contact-list__item">
        <svg class="contact-list__icon" viewBox="0 0 24 24" aria-hidden="true"><path d="M6.6 10.8a15.1 15.1 0 0 0 6.6 6.6l2.2-2.2a1 1 0 0 1 1-.25 11.4 11.4 0 0 0 3.6.57 1 1 0 0 1 1 1V20a1 1 0 0 1-1 1A17 17 0 0 1 3 4a1 1 0 0 1 1-1h3.5a1 1 0 0 1 1 1c0 1.25.2 2.45.57 3.57a1 1 0 0 1-.25 1z"/></svg>
        +351 936204518
      </li>
      <li class="contact-list__item">
        <svg class="contact-list__icon" viewBox="0 0 24 24" aria-hidden="true"><path d="M2 5h20v14H2z M4 7v.5l8 5 8-5V7z" fill-rule="evenodd"/></svg>
        famaral@nobrelentelusitana.example
      </li>
      <li class="contact-list__item">
        <svg class="contact-list__icon" viewBox="0 0 24 24" aria-hidden="true"><circle cx="12" cy="12" r="11"/><path d="M1 12h22M12 1c4 4 4 18 0 22M12 1c-4 4-4 18 0 22" stroke="#fbfbfb" stroke-width="1.6" fill="none"/></svg>
        www.nobrelentelusitana.example
      </li>
    </ul>
  </article>

  <article class="card card--back">
    <p class="brand-name">Nobre<br>Lente<br>Lusitana</p>
  </article>
</body>
</html>
```